Trevik Builders Business Card Design Project

Clean sharp business card
Ability to write on back of card
Details for the card -
Address: PO Box 5087, Kendrow, Qld, 4396
ABN: 47 305 921 276
BSA LIC 6825170
Ph: 07 4651 2839
Fax: 07 4651 2840
Email: trevikbuilders@quillpost.net

Reason: Time to review designs after weekend

```html
<!DOCTYPE html>
<html lang="en">
<head>
<meta charset="utf-8">
<title>Trevik Builders – Business Card</title>
<link rel="stylesheet" href="https://fonts.googleapis.com/css2?family=Open+Sans:wght@400;600&family=Arimo:wght@400&display=swap">
<style>
  :root {
    --page: #ffffff;
    --card-edge: #0a0a0a;
    --black: #060707;
    --maroon-deep: #160404;
    --maroon-dark: #220706;
    --maroon: #2e0a08;
    --maroon-bright: #561512;
    --arc: #40120c;
    --accent: #e8781e;
    --silver: #c9cbcd;
    --text: #ffffff;
  }
  * { margin: 0; padding: 0; box-sizing: border-box; }
  html, body {
    width: 1200px; height: 752px; overflow: hidden;
    background: var(--page);
  }
  .card {
    position: relative;
    width: 1200px; height: 752px;
    border-radius: 36px;
    overflow: hidden;
    border: 2px solid var(--card-edge);
    background: linear-gradient(90deg, var(--maroon-deep) 0%, var(--maroon-dark) 60%, var(--maroon) 85%, var(--maroon-bright) 100%);
    font-family: "Open Sans", Arial, sans-serif;
    color: var(--text);
  }
  .card-art { position: absolute; inset: 0; width: 100%; height: 100%; }
  .holder-name {
    position: absolute; left: 791px; top: 92px;
    font-family: "Arimo", Arial, sans-serif;
    font-size: 56px; font-weight: 400; letter-spacing: 0.5px;
    line-height: 1;
  }
  .brand {
    position: absolute; left: 212px; top: 208px;
    display: flex; align-items: center; gap: 14px;
    font-size: 38px; font-weight: 600; color: var(--silver);
    line-height: 1.2;
  }
  .brand-dot {
    width: 22px; height: 22px; border-radius: 50%;
    background: var(--accent);
  }
  .details {
    position: absolute; top: 432px;
    font-size: 29px; line-height: 40px;
    white-space: nowrap;
  }
  .details-postal { left: 43px; }
  .details-contact { left: 433px; top: 428px; }
  .divider {
    position: absolute; left: 390px; top: 386px;
    width: 4px; height: 208px;
    background: linear-gradient(180deg, #111 0%, #d8d8d8 30%, #555 60%, #111 100%);
  }
  .edge-glint {
    position: absolute; left: 22px; top: 100px;
    width: 3px; height: 540px;
    background: linear-gradient(180deg, transparent 0%, #9a9a9a 40%, #d0d0d0 55%, transparent 100%);
    opacity: .7;
  }
</style>
</head>
<body>
<main class="card">
  <svg class="card-art" viewBox="0 0 1200 752" aria-hidden="true">
    <defs>
      <radialGradient id="lowerGlow" cx="330" cy="640" r="520" gradientUnits="userSpaceOnUse">
        <stop offset="0" stop-color="#34383a"/>
        <stop offset="0.6" stop-color="#1a1c1d"/>
        <stop offset="1" stop-color="#060707"/>
      </radialGradient>
      <clipPath id="darkPanel">
        <path d="M0,0 L420,0 C760,50 900,300 855,470 C810,640 560,752 280,752 L0,752 Z"/>
      </clipPath>
    </defs>
    <path d="M430,0 C780,40 930,300 880,480 C830,660 560,760 280,770" fill="none" stroke="var(--arc)" stroke-width="16"/>
    <path d="M0,0 L420,0 C760,50 900,300 855,470 C810,640 560,752 280,752 L0,752 Z" fill="var(--black)"/>
    <path clip-path="url(#darkPanel)" d="M0,470 C250,330 600,250 900,265 L900,752 L0,752 Z" fill="url(#lowerGlow)"/>
  </svg>

  <div class="edge-glint"></div>

  <h1 class="holder-name">YOUR NAME</h1>

  <div class="brand">
    <span class="brand-dot"></span>
    <span class="brand-name">Trevik Builders</span>
  </div>

  <div class="details details-postal">
    <p>Address : PO Box 5087,</p>
    <p>Kendrow, Qld, 4396</p>
    <p>ABN :&nbsp; 47 305 921 276</p>
    <p>BAS LIC 6825170</p>
  </div>

  <div class="divider"></div>

  <div class="details details-contact">
    <p>Tel : 46512839</p>
    <p>Fax :&nbsp; 46512840</p>
    <p>E :&nbsp; trevikbuilders@quillpost.net</p>
  </div>
</main>
</body>
</html>
```